New landing page

We have an existing design at www.hostcorvel.com but we are not set on that design and probably want something different.
We want to increase conversion rates and experiment with a new landing page for our brightlisting promos campains.
We want to use a more single page long design page that contains these elements on one page:

Header
Images/headline
4 offer boxes
Features
Locations (map)
Testimonials
Why HostCorvel
Footer menu

Note should also be taken of research done by Pagetrove like this:
http://pagetrove.com/landing-page-articles/the-anatomy-of-a-landing-page/

Industry/Entity Type

Brightlisting

```html
<!DOCTYPE html>
<html lang="en">
<head>
<meta charset="utf-8">
<title>HostCorvel – Your own Linux Server in 59 seconds</title>
<link rel="stylesheet" href="https://fonts.googleapis.com/css2?family=Open+Sans:wght@300;400;600;700&family=Roboto:wght@300;400;500&display=swap">
<style>
:root{
  --black:#111214;
  --nav-active:#3a3b3d;
  --yellow:#f6b60f;
  --orange:#e9a100;
  --dark-band:#474747;
  --white:#ffffff;
  --text:#333333;
  --muted:#777777;
  --green:#2e7d1f;
  --red:#c8161d;
  --blue:#1577b8;
  --gold:#e2a30a;
  --card-border:#e3e3e3;
  --pale:#eef1f5;
  --why-bg:#f4f4f6;
}
*{box-sizing:border-box;margin:0;padding:0}
html,body{width:1200px;height:4027px;overflow:hidden}
body{font-family:"Open Sans",Arial,sans-serif;color:var(--text);background:var(--white);position:relative}
a{text-decoration:none;color:inherit}

/* Header */
.site-header{position:absolute;top:0;left:0;width:1200px;height:80px;background:var(--black)}
.brand{position:absolute;left:70px;top:18px;display:flex;align-items:center;gap:12px;color:var(--white);font-size:32px;font-weight:700;letter-spacing:-.5px}
.brand-dot{width:40px;height:40px;border-radius:50%;background:var(--yellow)}
.main-nav{position:absolute;right:70px;top:0;height:80px;display:flex;align-items:center}
.main-nav a{color:var(--white);font-size:15px;font-weight:600;padding:0 22px;height:80px;line-height:80px;position:relative}
.main-nav a.active{background:var(--nav-active)}
.main-nav a.active::after{content:"";position:absolute;left:50%;bottom:0;margin-left:-8px;border:8px solid transparent;border-bottom-color:var(--white)}
.main-nav a.nav-cta{background:var(--yellow);height:32px;line-height:32px;padding:0 14px;margin-left:10px;font-size:13px;border-radius:2px}

/* Hero */
.hero{position:absolute;top:80px;left:0;width:1200px;height:586px}
.hero-photo{position:absolute;inset:0;background:linear-gradient(90deg,#8e8f92 0%,#b8b9bb 35%,#d9d9d8 55%,#e9e2d6 72%,#f0a44a 85%,#e9e6e0 100%)}
.hero-copy{position:absolute;left:80px;top:128px;width:560px;color:var(--white)}
.hero-copy h1{font-family:"Roboto",Arial,sans-serif;font-weight:400;font-size:48px;line-height:54px;color:#111}
.hero-copy p{margin-top:28px;font-size:22px;line-height:30px;color:#f4f4f4}
.btn{display:inline-block;background:var(--yellow);color:var(--white);font-weight:600;text-align:center;border-radius:2px}
.hero-copy .btn{margin-top:28px;width:136px;height:46px;line-height:46px;font-size:18px}

/* Offers */
.offers{position:absolute;top:666px;left:0;width:1200px;height:644px;background:var(--dark-band);text-align:center;color:var(--white)}
.section-title{font-family:"Roboto",Arial,sans-serif;font-weight:400;font-size:48px;line-height:56px}
.section-sub{font-family:"Roboto",Arial,sans-serif;font-weight:300;font-size:25px;letter-spacing:1px;margin-top:4px}
.offers .section-title{padding-top:44px}
.plan{position:absolute;top:193px;width:228px;height:377px;background:var(--white);color:var(--text);text-align:center}
.plan.custom{top:204px}
.plan h3{font-weight:400;font-size:32px;margin-top:24px;color:#222}
.plan h3 span{font-weight:400}
.plan .ram{font-size:13px;margin-top:4px;color:#555}
.plan .ram b{font-weight:700}
.plan ul{list-style:none;margin-top:26px;font-size:13px;line-height:19px;color:#666}
.plan ul li.hl{font-weight:700}
.plan .price{position:absolute;left:0;bottom:0;width:100%;height:140px;background:#f4f4f4;text-align:left;padding:18px 0 0 54px}
.plan .from{font-size:12px;font-weight:700;color:#333}
.plan .amount{font-size:52px;line-height:52px;color:#222}
.plan .amount sup{font-size:22px;vertical-align:top;line-height:30px}
.plan .amount small{font-size:15px;color:#666}
.plan .order{display:block;width:120px;height:30px;line-height:30px;margin-top:8px;color:var(--white);font-size:12px;font-weight:700;border-radius:3px;text-align:center}
.plan .compare{font-size:11px;color:#999;margin-top:6px}
.budget{left:115px}.budget h3 span,.budget li.hl{color:var(--green)}.budget .ram b{color:var(--green)}.budget .order{background:var(--green)}
.extreme{left:368px}.extreme h3 span,.extreme li.hl{color:var(--red)}.extreme .ram b{color:var(--red)}.extreme .order{background:var(--red)}
.custom{left:628px}.custom h3 span,.custom li.hl{color:var(--blue)}.custom .order{background:var(--blue)}
.panel{left:883px}.panel h3 span,.panel li.hl{color:var(--gold)}.panel .ram b{color:var(--gold)}.panel .order{background:var(--gold)}

/* Features */
.features{position:absolute;top:1310px;left:0;width:1200px;height:1227px;text-align:center;color:#111}
.features .section-title{padding-top:42px}
.features .section-sub{color:#222}
.feature{position:absolute;width:258px;height:260px;border:1px solid var(--card-border);box-shadow:0 1px 3px rgba(0,0,0,.05);padding:36px 22px 0}
.feature .icon{width:70px;height:70px;border-radius:50%;margin:0 auto}
.feature h4{font-size:13px;font-weight:700;margin-top:26px;color:#222}
.feature p{font-size:12px;line-height:19px;color:#777;margin-top:12px}
.col1{left:185px}.col2{left:467px}.col3{left:749px}
.row1{top:188px}.row2{top:476px}.row3{top:763px}
.cta-band{position:absolute;left:419px;top:1058px;width:352px;height:76px;background:var(--orange);color:var(--white);font-weight:600;padding-top:12px}
.cta-band span{display:block;font-size:16px}
.cta-band strong{display:block;font-size:22px;font-weight:600;margin-top:2px}

/* Why us */
.why{position:absolute;top:2537px;left:0;width:1200px;height:390px;background:var(--why-bg)}
.why-photo{position:absolute;left:0;top:0;width:612px;height:390px;background:linear-gradient(90deg,#7a5c3f 0%,#c9a985 30%,#e8dccd 60%,#f2efea 100%)}
.why-copy{position:absolute;left:665px;top:88px;width:450px}
.why-copy h2{font-family:"Roboto",Arial,sans-serif;font-weight:400;font-size:44px;color:#111}
.why-copy p{font-size:14px;line-height:21px;color:#333;margin-top:16px}
.why-copy .btn{margin-top:22px;width:135px;height:46px;line-height:46px;font-size:17px}

/* Testimonials */
.testimonials{position:absolute;top:2927px;left:0;width:1200px;height:585px;background:var(--pale);text-align:center}
.t-title{position:absolute;top:65px;left:0;width:1200px;font-family:"Open Sans",Arial,sans-serif;font-weight:300;font-size:34px;letter-spacing:2px;color:#555}
.t-title::before,.t-title::after{content:"";display:inline-block;width:56px;height:1px;background:#777;vertical-align:middle;margin:0 18px}
.avatar{position:absolute;border-radius:50%;background:radial-gradient(circle at 50% 45%,#c9b7a6,#7d746e)}
.a1{left:393px;top:172px;width:62px;height:62px}
.a2{left:507px;top:152px;width:94px;height:94px;border:4px solid var(--white)}
.a3{left:648px;top:172px;width:62px;height:62px;background:radial-gradient(circle,#d7e3e6,#8fa7ad)}
.a4{left:762px;top:172px;width:62px;height:62px}
.quote-mark{position:absolute;top:272px;left:0;width:1200px;font-size:40px;color:#aaa;font-family:Georgia,serif}
.quote{position:absolute;top:330px;left:230px;width:740px;font-size:15px;line-height:22px;color:#333}
.t-rule{position:absolute;top:432px;left:572px;width:56px;height:1px;background:#777}
.t-name{position:absolute;top:458px;left:0;width:1200px;font-size:14px;font-weight:600;color:#222}
.t-role{position:absolute;top:480px;left:0;width:1200px;font-size:13px;color:#2a9fd6}

/* Contact */
.contact{position:absolute;top:3512px;left:0;width:1200px;height:430px}
.map{position:absolute;inset:0;background:linear-gradient(135deg,#e4e4e4,#d2d2d2 50%,#e9e9e9)}
.contact-panel{position:absolute;left:67px;top:0;width:330px;height:430px;background:var(--orange);padding:24px 27px}
.contact-panel h2{font-family:"Open Sans",Arial,sans-serif;font-weight:300;font-size:36px;color:var(--white)}
.field{display:block;width:284px;height:44px;border:2px solid var(--white);color:var(--white);font-size:14px;padding:10px 12px;margin-top:10px}
.field.first{margin-top:18px}
.field.message{height:92px}
.send{display:block;margin-top:18px;width:135px;height:34px;line-height:34px;background:var(--white);color:#333;font-size:14px;font-weight:700;text-align:center}

/* Footer */
.site-footer{position:absolute;top:3942px;left:0;width:1200px;height:85px;background:var(--white)}
.foot-nav{position:absolute;left:86px;top:20px;font-size:13px;color:#333}
.copyright{position:absolute;left:86px;top:46px;font-size:12px;color:#333}
.social{position:absolute;right:80px;top:22px;display:flex;gap:12px}
.social span{width:34px;height:34px;border-radius:50%;background:#333}
</style>
</head>
<body>

<header class="site-header">
  <a class="brand" href="#"><span class="brand-dot"></span>HostCorvel</a>
  <nav class="main-nav">
    <a class="active" href="#">Home</a>
    <a href="#offers">Offers</a>
    <a href="#features">Features</a>
    <a href="#why">Why Us</a>
    <a href="#locations">Locations</a>
    <a class="nav-cta" href="#offers">Order Now</a>
  </nav>
</header>

<section class="hero">
  <div class="hero-photo" role="img" aria-label="Woman in an orange top working on a laptop with a glass of juice in a bright room"></div>
  <div class="hero-copy">
    <h1>Your own Linux Server in 59 seconds</h1>
    <p>With 24x7x365 support, instant setup and upgrades, 99% uptime and our 14 day no questions asked money back gurantee.</p>
    <a class="btn" href="#offers">Order Now</a>
  </div>
</section>

<section class="offers" id="offers">
  <h2 class="section-title">Our Offers</h2>
  <p class="section-sub">Loremipsum Dolar sit amet is a dummy text</p>

  <div class="plan budget">
    <h3>Budget <span>VPS</span></h3>
    <p class="ram"><b>256 MB</b> Guaranteed RAM</p>
    <ul><li>1x 3.4 Ghz Cores</li><li>10 GB Raid-10 Storage</li><li>300 GB Bandwidth</li><li>Linux of your choice</li><li class="hl">59 second Activation</li></ul>
    <div class="price"><p class="from">FROM</p><p class="amount"><sup>$</sup>10<small> / month</small></p><a class="order" href="#">ORDER NOW</a><p class="compare">compare budget vps</p></div>
  </div>

  <div class="plan extreme">
    <h3>Extreme <span>VPS</span></h3>
    <p class="ram"><b>2048 MB</b> Guaranteed RAM</p>
    <ul><li>4x 3.4 Ghz Cores</li><li>100 GB Raid-10 Storage</li><li>3000 GB Bandwidth</li><li>Linux of your choice</li><li class="hl">59 second Activation</li></ul>
    <div class="price"><p class="from">FROM</p><p class="amount"><sup>$</sup>40<small> / month</small></p><a class="order" href="#">ORDER NOW</a><p class="compare">compare extreme vps</p></div>
  </div>

  <div class="plan custom">
    <h3>Custom <span>VPS</span></h3>
    <p class="ram">Customize your RAM</p>
    <ul><li>Customize CPU</li><li>Customize Storage</li><li>Customize Bandwidth</li><li>Linux of your choice</li><li class="hl">59 second Activation</li></ul>
    <div class="price"><p class="from">FROM</p><p class="amount"><sup>$</sup>10<small> / month</small></p><a class="order" href="#">ORDER NOW</a></div>
  </div>

  <div class="plan panel">
    <h3>ControlDeck <span>VPS</span></h3>
    <p class="ram"><b>1024 MB</b> Guaranteed RAM</p>
    <ul><li>4x 3.4 Ghz Cores</li><li>50 GB Raid-10 Storage</li><li>1500 GB Bandwidth</li><li>ControlDeck auto installed</li><li class="hl">59 second Activation</li></ul>
    <div class="price"><p class="from">FROM</p><p class="amount"><sup>$</sup>45<small> / month</small></p><a class="order" href="#">ORDER NOW</a></div>
  </div>
</section>

<section class="features" id="features">
  <h2 class="section-title">VPS Hosting Features</h2>
  <p class="section-sub">Loremipsum Dolar sit amet is a dummy text</p>

  <div class="feature col1 row1"><div class="icon" style="background:#5cae2e"></div><h4>59 Second Activation</h4><p>Your virtual host will be activated immediately after your first payment, so you dont wait.</p></div>
  <div class="feature col2 row1"><div class="icon" style="background:#2e9be0"></div><h4>99.9% Uptime</h4><p>We guarantee your VPS will have an uptime of 99.9% and strive for 100%.</p></div>
  <div class="feature col3 row1"><div class="icon" style="background:#f0a400"></div><h4>Full Root Access</h4><p>Just like having your own dedicated server but cheaper than ever. Even custom kernels are supported.</p></div>

  <div class="feature col1 row2"><div class="icon" style="background:#f3d000"></div><h4>24/7/365 Support</h4><p>We're here 24/7, weekends, holidays, day and night to assist you.</p></div>
  <div class="feature col2 row2"><div class="icon" style="background:#e05a8a"></div><h4>Global Locations</h4><p>We have servers located all over the world for you to choose from. Check our locations page</p></div>
  <div class="feature col3 row2"><div class="icon" style="background:#3a8fe0"></div><h4>Choice of operating systems</h4><p>We specialize in Linux VPSs. The latest and older releases of Corvix, Ubira, Debrin, Opalux are available.</p></div>

  <div class="feature col1 row3"><div class="icon" style="background:#c2231c"></div><h4>ControlDeck Suite</h4><p>You can order ControlDeck for $15 per month on any of our VPSs that have 1024MB or more of RAM. We will install the latest</p></div>
  <div class="feature col2 row3"><div class="icon" style="background:#e08a2a"></div><h4>IP Adresses</h4><p>All plans include 1 x IPv4 address. Upto 10 Additional IPv4 addresses may be ordered. Beyond 10 you need to request via email with a</p></div>
  <div class="feature col3 row3"><div class="icon" style="background:#2f7a2a"></div><h4>Upgrades with no downtime</h4><p>On all our non KVM plans you can easily upgrade your ram, disk or CPU with no downtime at all. KVM plans will require a quick reboot.</p></div>

  <a class="cta-band" href="#offers"><span>Get started today with a</span><strong>14 Day Money Back Gurantee</strong></a>
</section>

<section class="why" id="why">
  <div class="why-photo" role="img" aria-label="Smiling woman with a laptop and a coffee cup at a cafe window"></div>
  <div class="why-copy">
    <h2>Why Us?</h2>
    <p>All plans include 1 x IPv4 address. Upto 10 Additional IPv4 addresses may be ordered. Beyond 10 you need to request via email with a detailed description. IPv6's addresses are also available at some of our data centeres on request. Reverse DNS entries are available for all IPs.</p>
    <a class="btn" href="#offers">Order Now</a>
  </div>
</section>

<section class="testimonials">
  <h2 class="t-title">TESTIMONIALS</h2>
  <div class="avatar a1" role="img" aria-label="Customer portrait"></div>
  <div class="avatar a2" role="img" aria-label="Portrait of the featured customer"></div>
  <div class="avatar a3" role="img" aria-label="Customer portrait"></div>
  <div class="avatar a4" role="img" aria-label="Customer portrait"></div>
  <div class="quote-mark">&ldquo;</div>
  <p class="quote">Lorem ipsum dolor sit amet, consectetur adipiscing elit. Nulla eget dapibus quam, vel ornare velit. In sed mi vel diam ullamcorper rutrum non sed libero. Nunc sit amet aliquet diam, vitae hendrerit dui. Pellentesque elit risus, feugiat sit amet scelerisque et, semper ac odio. Aenean ullamcorper bibilusendum, eget euismod mi pharetra.</p>
  <div class="t-rule"></div>
  <p class="t-name">Lena Marsholt</p>
  <p class="t-role">CEO, Tallfern Web</p>
</section>

<section class="contact" id="locations">
  <div class="map" role="img" aria-label="Street map showing data centre locations"></div>
  <form class="contact-panel">
    <h2>Contact Us Now</h2>
    <span class="field first">Name</span>
    <span class="field">Company</span>
    <span class="field">Email</span>
    <span class="field message">Message</span>
    <span class="send">Send Now</span>
  </form>
</section>

<footer class="site-footer">
  <p class="foot-nav">Home &nbsp;|&nbsp; Offers &nbsp;|&nbsp; Features &nbsp;|&nbsp; Why Us &nbsp;|&nbsp; Locations</p>
  <p class="copyright">Copyright 2014 All Rights Reserved</p>
  <div class="social" aria-label="Social links"><span></span><span></span><span></span><span></span></div>
</footer>

</body>
</html>
```